Home Multi-Service Company Website

I currently have only a landing page but am looking for someone to build out a nice, modern looking website that will cover multiple services we offer like Landscape Lighting, Gutter Cleaning, Holiday Lighting, Window Cleaning, Insulation Services like Blow In and Removal, Blower Door Tests, Rodent Exclusion and Trapping and others. We would also like our Holiday lighting category to have links to a separate page for franchise opportunities.

Target Market(s)

Home

Font styles to use
Serif
Sans Serif

Requirements
Must have
• A modern and organized look. Detailed information regarding each service provided by our company.
Nice to have
• We are a service company so would like to see options to link reviews from quorvel and maybe some nice pictures of people at home. We would like the color to match our logo as well.

```html
<!DOCTYPE html>
<html lang="en">
<head>
<meta charset="utf-8">
<title>Hearthline Services — Home Multi-Service Company</title>
<link href="https://fonts.googleapis.com/css2?family=Lato:ital,wght@0,400;0,700;0,900;1,400&display=swap" rel="stylesheet">
<style>
:root{
  --orange:#f07c1e;
  --navy:#2f3552;
  --text:#4a4a4a;
  --white:#ffffff;
  --footer:#2b2b2b;
  --footer-text:#c9c9c9;
}
*{margin:0;padding:0;box-sizing:border-box}
html,body{width:1200px;height:4063px;overflow:hidden}
body{position:relative;font-family:'Lato',sans-serif;color:var(--text);background:var(--white)}
.abs{position:absolute}
.center{left:0;width:1200px;text-align:center}

/* header */
.site-header{position:absolute;left:0;top:0;width:1200px;height:120px;background:var(--white)}
.brand{position:absolute;left:74px;top:34px;display:flex;align-items:center;gap:10px;font-weight:900;font-size:30px;color:var(--navy);letter-spacing:.5px}
.brand-dot{width:26px;height:26px;border-radius:50%;background:var(--navy)}
.nav{position:absolute;top:52px;font-size:12.5px;font-weight:700;color:#333;letter-spacing:.3px}
.nav a{position:absolute;white-space:nowrap;color:inherit;text-decoration:none;transform:translateX(-50%)}
.nav .active::after{content:"";position:absolute;left:-14px;right:-14px;top:22px;height:2px;background:var(--orange)}
.social{position:absolute;display:flex;gap:20px}
.social span{width:18px;height:18px;border-radius:50%;background:#333}

/* buttons */
.btn{position:absolute;left:520px;width:160px;height:40px;border-radius:20px;background:var(--orange);color:var(--white);font-weight:700;font-size:16px;line-height:40px;text-align:center}
.btn-outline{background:transparent;border:2px solid #333;color:#333;line-height:35px;height:39px}

/* photo areas */
.photo{position:absolute}
.hero{left:0;top:120px;width:1200px;height:795px;background:linear-gradient(180deg,#2c3a22 0%,#4a4a2a 35%,#3b5a22 65%,#4f7a2a 100%)}
.franchise{left:0;top:1355px;width:1200px;height:493px;background:radial-gradient(ellipse at 40% 60%,#4a2a18 0%,#2a1c14 45%,#1a1410 100%)}
.testimonial{left:0;top:2544px;width:1200px;height:493px;background:linear-gradient(180deg,#3e4a3e 0%,#4d5a48 45%,#3e5a2c 75%,#2f4a22 100%)}

.hero-title{top:450px;font-size:82px;font-weight:700;color:var(--white)}
.hero-sub{top:544px;font-size:30px;font-weight:700;color:var(--white)}

.section-title{font-size:33px;font-weight:700;color:var(--navy)}
.welcome-text{top:1040px;font-size:16.5px;line-height:33px;color:var(--text)}

.band-title{top:1494px;font-size:34px;font-weight:700;color:var(--white)}
.band-text{top:1556px;font-size:16.5px;line-height:33px;color:var(--white)}

.card-img{position:absolute;width:331px}
.card-title{position:absolute;width:331px;text-align:center;font-size:23px;font-weight:700;color:var(--orange);text-transform:uppercase}
.card-text{position:absolute;width:331px;text-align:center;font-size:16.5px;line-height:28.6px;color:var(--text)}

.stars{position:absolute;left:529px;top:2700px;display:flex;gap:9px}
.quote{top:2729px;font-size:17px;line-height:33px;font-style:italic;color:var(--white)}
.quote-name{top:2852px;font-size:15px;font-weight:700;color:var(--white)}

/* footer */
.site-footer{position:absolute;left:0;top:3695px;width:1200px;height:368px;background:var(--footer)}
.f-col{position:absolute;top:92px}
.f-col h4{font-size:16px;font-weight:900;color:var(--white);margin-bottom:6px}
.f-col li{list-style:none;font-size:14px;color:var(--footer-text)}
.f-map li{line-height:27.6px}
.f-serv li{line-height:34px}
.f-brand{position:absolute;left:856px;top:155px;display:flex;align-items:center;gap:8px;font-size:26px;font-weight:900;color:var(--white)}
.f-brand .brand-dot{width:20px;height:20px;background:var(--white)}
.copyright{position:absolute;left:856px;top:229px;font-size:13px;line-height:24px;color:var(--footer-text)}
.site-footer .social span{background:#d0d0d0}
</style>
</head>
<body>

<header class="site-header">
  <div class="brand"><span class="brand-dot"></span>Hearthline</div>
  <nav class="nav">
    <a class="active" style="left:416px">HOME</a>
    <a style="left:505px">SERVICES</a>
    <a style="left:605px">ABOUT US</a>
    <a style="left:692px">BLOG</a>
    <a style="left:777px">REVIEWS</a>
    <a style="left:874px">CONTACT</a>
  </nav>
  <div class="social" style="left:960px;top:50px" aria-label="Social links"><span></span><span></span><span></span><span></span><span></span></div>
</header>

<div class="photo hero" role="img" aria-label="Evening garden with landscape lighting along a stone path beside a house"></div>
<h1 class="abs center hero-title">Hearthline Services</h1>
<p class="abs center hero-sub">We are a Home Multi-Service Company.</p>
<a class="btn" style="top:609px">Read More</a>

<h2 class="abs center section-title" style="top:980px">WELCOME TO HEARTHLINE SERVICES</h2>
<p class="abs center welcome-text">Sed ut perspiciatis unde omnis iste natus error sit voluptatem accusantium doloremque laudantium, totam rem aperiam, eaque ipsa quae<br>ab illo inventore veritatis et quasi architecto beatae vitae dicta sunt explicabo. Nemo enim ipsam voluptatem quia voluptas sit aspernatur<br>aut odit aut fugit, sed quia consequuntur magni dolores eos qui ratione voluptatem sequi nesciunt. Neque porro quisquam est,<br>qui dolorem ipsum quia dolor sit amet, consectetur, adipisci velit, sed quia non numquam eius modi tempora incidunt ut labore<br>et dolore magnam aliquam quaerat voluptatem.</p>
<a class="btn" style="top:1241px">Read More</a>

<div class="photo franchise" role="img" aria-label="Cosy living room with fireplace and lit Christmas tree"></div>
<h2 class="abs center band-title">FRANCHISE OPPORTUNITIES</h2>
<p class="abs center band-text">Nemo enim ipsam voluptatem quia voluptas sit aspernatur aut odit aut fugit, sed quia consequuntur magni dolores<br>eos qui ratione voluptatem sequi nesciunt.</p>
<a class="btn" style="top:1656px">Read More</a>

<h2 class="abs center section-title" style="top:1899px">OUR SERVICES</h2>
<div class="card-img" style="left:74px;top:1981px;height:208px;background:linear-gradient(180deg,#2e3a24,#4f6a2a)" role="img" aria-label="Garden path with landscape lights at dusk"></div>
<div class="card-img" style="left:435px;top:1981px;height:208px;background:linear-gradient(135deg,#6b4a3a,#e9e6e0 55%,#5a7a3a)" role="img" aria-label="Worker on a ladder cleaning house gutters"></div>
<div class="card-img" style="left:796px;top:1981px;height:208px;background:linear-gradient(90deg,#cfd8e0,#4a6a9a 60%,#e8eaec)" role="img" aria-label="Worker in blue cleaning a window"></div>
<h3 class="card-title" style="left:74px;top:2213px">Landscape Lighting</h3>
<h3 class="card-title" style="left:435px;top:2213px">Gutter Cleaning</h3>
<h3 class="card-title" style="left:796px;top:2213px">Window Cleaning</h3>
<p class="card-text" style="left:74px;top:2251px">Sed ut perspiciatis unde omnis iste natus<br>error sit voluptatem accusantium<br>doloremque laudantium, totam rem<br>aperiam, eaque ipsa quae.</p>
<p class="card-text" style="left:435px;top:2251px">Sed ut perspiciatis unde omnis iste natus<br>error sit voluptatem accusantium<br>doloremque laudantium, totam rem<br>aperiam, eaque ipsa quae.</p>
<p class="card-text" style="left:796px;top:2251px">Sed ut perspiciatis unde omnis iste natus<br>error sit voluptatem accusantium<br>doloremque laudantium, totam rem<br>aperiam, eaque ipsa quae.</p>
<a class="btn btn-outline" style="top:2425px">View All</a>

<div class="photo testimonial" role="img" aria-label="Family relaxing together on a green lawn at home"></div>
<div class="stars" aria-label="Five star rating">
  <svg width="20" height="20" viewBox="0 0 20 20"><polygon points="10,1 12.6,7 19,7.4 14,11.6 15.6,18 10,14.5 4.4,18 6,11.6 1,7.4 7.4,7" fill="#f07c1e"/></svg>
  <svg width="20" height="20" viewBox="0 0 20 20"><polygon points="10,1 12.6,7 19,7.4 14,11.6 15.6,18 10,14.5 4.4,18 6,11.6 1,7.4 7.4,7" fill="#f07c1e"/></svg>
  <svg width="20" height="20" viewBox="0 0 20 20"><polygon points="10,1 12.6,7 19,7.4 14,11.6 15.6,18 10,14.5 4.4,18 6,11.6 1,7.4 7.4,7" fill="#f07c1e"/></svg>
  <svg width="20" height="20" viewBox="0 0 20 20"><polygon points="10,1 12.6,7 19,7.4 14,11.6 15.6,18 10,14.5 4.4,18 6,11.6 1,7.4 7.4,7" fill="#f07c1e"/></svg>
  <svg width="20" height="20" viewBox="0 0 20 20"><polygon points="10,1 12.6,7 19,7.4 14,11.6 15.6,18 10,14.5 4.4,18 6,11.6 1,7.4 7.4,7" fill="#f07c1e"/></svg>
</div>
<p class="abs center quote">“&nbsp;Sed ut perspiciatis unde omnis iste natus error sit voluptatem accusantium doloremque laudantium, totam<br>rem aperiam, eaque ipsa quae ab illo inventore veritatis et quasi architecto beatae vitae dicta sunt<br>Nemo enim ipsam voluptatem quia voluptas sit aspernatur aut odit aut fugi....”</p>
<p class="abs center quote-name">NAME HEADING</p>

<h2 class="abs center section-title" style="top:3096px">INSULATION SERVICES</h2>
<div class="card-img" style="left:74px;top:3182px;height:210px;background:linear-gradient(135deg,#2a3040,#e8ecef 55%,#d6b82a)" role="img" aria-label="Person operating a yellow snow blower"></div>
<div class="card-img" style="left:435px;top:3182px;height:210px;background:linear-gradient(180deg,#b01e28 0%,#c8c4bc 55%,#e4e2de)" role="img" aria-label="Technician setting up blower door test equipment"></div>
<div class="card-img" style="left:796px;top:3182px;height:210px;background:linear-gradient(135deg,#e8ecf2,#7a8aa8 55%,#d8dde6)" role="img" aria-label="Wire mesh rodent guard fitted over a siding vent"></div>
<h3 class="card-title" style="left:74px;top:3425px">Blow In and Removal</h3>
<h3 class="card-title" style="left:435px;top:3425px">Blower Door Tests</h3>
<h3 class="card-title" style="left:796px;top:3425px">Rodent Exclusion</h3>
<p class="card-text" style="left:74px;top:3464px">Sed ut perspiciatis unde omnis iste<br>natus error sit voluptatem<br>accusantium&nbsp; doloremque<br>laudantium, totam rem&nbsp; aperiam,<br>eaque ipsa quae.</p>
<p class="card-text" style="left:435px;top:3464px">Sed ut perspiciatis unde omnis iste<br>natus error sit voluptatem<br>accusantium&nbsp; doloremque<br>laudantium, totam rem&nbsp; aperiam,<br>eaque ipsa quae.</p>
<p class="card-text" style="left:796px;top:3464px">Sed ut perspiciatis unde omnis iste<br>natus error sit voluptatem<br>accusantium&nbsp; doloremque<br>laudantium, totam rem&nbsp; aperiam,<br>eaque ipsa quae.</p>

<footer class="site-footer">
  <div class="f-col f-map" style="left:93px"><h4>SITE MAP</h4><ul><li>Home</li><li>Services</li><li>About Us</li><li>Blog</li><li>Reviews</li><li>Contact</li></ul></div>
  <div class="f-col f-serv" style="left:306px"><h4>SERVICES</h4><ul><li>Landscape Lighting</li><li>Gutter Cleaning</li><li>Holiday Lighting</li><li>Window Cleaning</li></ul></div>
  <div class="f-col f-serv" style="left:577px"><h4>INSULATION SERVICES</h4><ul><li>Blow In and Removal</li><li>Blower Door Tests</li><li>Rodent Exclusion</li><li>Trapping</li></ul></div>
  <div class="social" style="left:854px;top:98px" aria-label="Social links"><span></span><span></span><span></span><span></span><span></span></div>
  <div class="f-brand"><span class="brand-dot"></span>Hearthline</div>
  <p class="copyright">Copyright © 2021. Company Name<br>All Right Reserved</p>
</footer>

</body>
</html>
```